Wedding page for Linda and Daniel

we need a webpage for our wedding. The website contains the basic information of the wedding. like general information, timetable, map, contact information and a photo section, more you find in the attached word document.
attached you see our invitation cards, design should have similarties like the cards.
We like green colours and as its a weeding page it can be romantic. :-)
Industry/Entity Type
Wedding
Coding
Coded - Design and coding required
Number of Pages Required
3 page
Font styles to use
Serif
Sans Serif
Decorative
Script
Colors
a5ce39
Requirements
Must have
- a clear structure and a simple navigation as there are 5 to 7 navigation points
- The weeding date should be clearly visible 26.05.2018.
- All labels and translation have to be editable by my (in HTML code or psd code is fine) --> the final page will be in german
Nice to have
- if the webdesign has some similarities with the wedding card.
- if there is a time counter till the wedding is coming.
- a modern way to display the program of the wedding day.
- the domain is kolvarenplitz.ch and would be cool to integrate somehow.
- if the website should be responsive.
Should not have
- no special logo or something needed.

```html
<!DOCTYPE html>
<html lang="en">
<head>
<meta charset="utf-8">
<title>Linda &amp; Daniel – Wedding</title>
<link href="https://fonts.googleapis.com/css2?family=Great+Vibes&family=Lora:wght@400;700&display=swap" rel="stylesheet">
<style>
:root{
  --green:#a5ce39;
  --green-dark:#8fb82a;
  --ink:#555;
  --muted:#888;
  --paper:#fafafa;
  --white:#fff;
  --line:#dcdcdc;
}
*{box-sizing:border-box;margin:0;padding:0}
html,body{width:1200px;height:3982px;overflow:hidden}
body{position:relative;background:var(--paper);font-family:"Lora",Georgia,serif;color:var(--ink)}
.abs{position:absolute}
.script{font-family:"Great Vibes",cursive}

/* hero */
.hero{left:0;top:0;width:1200px;height:717px;background:linear-gradient(160deg,#8a7a66 0%,#a8977f 35%,#9b8a73 60%,#6f6250 100%)}
.hero-inner{left:0;top:0;width:1200px;height:717px;text-align:center;color:var(--white)}
.hero-kicker{position:absolute;left:0;width:1200px;top:222px;font-size:44px}
.hero-names{position:absolute;left:0;width:1200px;top:280px;font-size:118px;line-height:1;display:flex;justify-content:center;align-items:center;gap:30px}
.hero-date{position:absolute;left:0;width:1200px;top:436px;font-size:32px;letter-spacing:1px}

/* nav */
.nav{left:0;top:717px;width:1200px;height:69px;background:var(--green)}
.nav-item{position:absolute;top:26px;font-size:14px;color:var(--white);transform:translateX(-50%);border-bottom:1px solid rgba(255,255,255,.8);padding-bottom:3px;white-space:nowrap}
.nav-home{position:absolute;left:252px;top:0;width:70px;height:69px;background:var(--white);color:#666;font-size:14px;font-weight:700;text-align:center;padding-top:12px}
.nav-home svg{display:block;margin:0 auto 6px}

/* section titles */
.sec-title{left:0;width:1200px;display:flex;justify-content:center;align-items:center;gap:12px;color:var(--green-dark)}
.sec-title .rule{width:60px;height:1px;background:var(--green)}
.sec-title h2{font-family:"Great Vibes",cursive;font-weight:400;font-size:38px;margin:0 8px}

/* countdown */
.count{top:967px;width:86px;text-align:center}
.count .ring{width:86px;height:86px;border:2px solid var(--green);border-radius:50%;display:flex;align-items:center;justify-content:center;font-size:30px;color:var(--green-dark)}
.count .lab{margin-top:16px;font-size:14px;color:var(--muted)}

/* couple */
.couple-band{left:0;top:1264px;width:1200px;height:621px;background:linear-gradient(90deg,#5f6f3a 0%,#8c8c74 35%,#c9c6b9 50%,#7f8b4f 70%,#4e6a28 100%)}
.portrait{top:1325px;width:306px;height:306px;border-radius:50%;border:4px solid var(--green);background:var(--white);padding:6px}
.portrait div{width:100%;height:100%;border-radius:50%}
.p-groom div{background:linear-gradient(160deg,#3b3433,#6d5a52 55%,#1f1c1c)}
.p-bride div{background:linear-gradient(160deg,#b0845c,#d7b291 55%,#8d6845)}
.person{top:1648px;width:360px;text-align:center;color:var(--white)}
.person h3{font-family:"Great Vibes",cursive;font-weight:400;font-size:50px;line-height:1}
.person p{margin-top:14px;font-size:13px;line-height:1.45}
.socials{display:flex;justify-content:center;gap:22px;margin-top:22px}
.socials span{width:10px;height:10px;border-radius:50%;background:var(--white)}

/* events */
.event{top:2058px;width:282px}
.event h3{font-weight:400;font-size:24px;color:var(--green-dark);padding-bottom:14px;border-bottom:1px solid var(--line)}
.event-row{display:flex;gap:14px;margin-top:22px}
.date-dot{flex:none;width:86px;height:86px;border-radius:50%;background:var(--green);border:4px solid #d7ebb0;color:var(--white);text-align:center;font-weight:700;font-size:15px;line-height:1.15;padding-top:12px}
.date-dot svg{display:block;margin:0 auto 3px}
.event-meta{font-size:14px;line-height:1.5;color:#666;padding-top:6px}
.event-meta div{display:flex;gap:6px;align-items:flex-start;margin-bottom:8px}
.event p{margin-top:14px;font-size:13px;line-height:1.5;color:var(--muted)}
.read-more{display:block;margin-top:14px;font-size:13px;color:#666}
.read-more b{color:var(--green-dark)}

/* album */
.album{left:0;top:2496px;width:1200px;height:557px;background:linear-gradient(100deg,#2f3a2a 0%,#6c7458 30%,#b8b7aa 48%,#6d8150 70%,#34482a 100%)}
.arrow{top:2712px}
.thumb{top:2985px}

/* rsvp */
.field{top:3324px;height:42px;border:1px solid var(--line);border-radius:21px;background:var(--white);font-size:13px;color:#999;padding:12px 20px}
.send{left:539px;top:3385px;width:126px;height:36px;border-radius:18px;background:var(--green);color:var(--white);font-size:13px;font-weight:700;letter-spacing:1px;text-align:center;line-height:36px}

/* footer */
.footer{left:0;top:3544px;width:1200px;height:438px;background:linear-gradient(180deg,#6e6656 0%,#8a7c68 40%,#6c7a47 80%,#4f6a2d 100%)}
.farewell{left:0;top:3708px;width:1200px;text-align:center;color:var(--white);font-size:54px;line-height:1.2}
.with{left:0;top:3782px;width:1200px;text-align:center;color:var(--green);font-size:20px}
.copy{left:0;top:3930px;width:1200px;text-align:center;color:var(--white);font-size:13px}
</style>
</head>
<body>

<div class="abs hero" role="img" aria-label="Photo of a heart drawn in beach sand with the couple's shadow"></div>
<header class="abs hero-inner">
  <p class="hero-kicker script">We are getting married!</p>
  <h1 class="hero-names script"><span>Linda</span>
    <svg width="110" height="96" viewBox="0 0 100 88"><path d="M50 86C20 62 2 46 2 26 2 12 13 2 26 2c10 0 19 6 24 15C55 8 64 2 74 2c13 0 24 10 24 24 0 20-18 36-48 60z" fill="#a5ce39"/></svg>
    <span>Daniel</span></h1>
  <p class="hero-date">26.05.2018</p>
</header>

<nav class="abs nav">
  <div class="nav-home"><svg width="14" height="12" viewBox="0 0 100 88"><path d="M50 86C20 62 2 46 2 26 2 12 13 2 26 2c10 0 19 6 24 15C55 8 64 2 74 2c13 0 24 10 24 24 0 20-18 36-48 60z" fill="#a5ce39"/></svg>Home</div>
  <span class="nav-item" style="left:380px">Our Story</span>
  <span class="nav-item" style="left:478px">Gallery</span>
  <span class="nav-item" style="left:597px">When &amp; Where</span>
  <span class="nav-item" style="left:714px">Events</span>
  <span class="nav-item" style="left:797px">Blogs</span>
  <span class="nav-item" style="left:895px">Contact Us</span>
</nav>

<div class="abs sec-title" style="top:896px"><span class="rule"></span>♥<h2>The Countdown begins!</h2>♥<span class="rule"></span></div>
<div class="abs count" style="left:290px"><div class="ring">02</div><div class="lab">Months</div></div>
<div class="abs count" style="left:427px"><div class="ring">17</div><div class="lab">Days</div></div>
<div class="abs count" style="left:557px"><div class="ring">23</div><div class="lab">Hours</div></div>
<div class="abs count" style="left:688px"><div class="ring">53</div><div class="lab">Minutes</div></div>
<div class="abs count" style="left:817px"><div class="ring">03</div><div class="lab">Seconds</div></div>

<div class="abs sec-title" style="top:1190px"><span class="rule"></span>♥<h2>Happy Couple</h2>♥<span class="rule"></span></div>
<div class="abs couple-band" role="img" aria-label="Soft-focus photo of the couple dancing outdoors on a lawn"></div>
<div class="abs portrait p-groom" style="left:152px"><div role="img" aria-label="Portrait photo of Daniel"></div></div>
<div class="abs portrait p-bride" style="left:736px"><div role="img" aria-label="Portrait photo of Linda"></div></div>
<svg class="abs" style="left:540px;top:1420px" width="140" height="110" viewBox="0 0 140 110">
  <path d="M82 106C50 82 30 64 30 42 30 27 42 16 56 16c11 0 20 6 26 16 6-10 15-16 26-16 14 0 26 11 26 26 0 22-20 40-52 64z" fill="#a5ce39" opacity=".45"/>
  <path d="M60 100C28 76 8 58 8 36 8 21 20 10 34 10c11 0 20 6 26 16 6-10 15-16 26-16 14 0 26 11 26 26 0 22-20 40-52 64z" fill="#a5ce39"/>
</svg>
<div class="abs person" style="left:125px"><h3>Daniel</h3>
  <p>Duis aute irure dolor in<br>reprehenderit in voluptate velit esse cillum<br>dolore eu fugiat nulla pariatur. Excepteur sint<br>occaecat cupidatat.</p>
  <div class="socials"><span></span><span></span><span></span></div></div>
<div class="abs person" style="left:709px"><h3>Linda</h3>
  <p>Duis aute irure dolor in<br>reprehenderit in voluptate velit esse cillum<br>dolore eu fugiat nulla pariatur. Excepteur sint<br>occaecat cupidatat.</p>
  <div class="socials"><span></span><span></span><span></span></div></div>

<div class="abs sec-title" style="top:1992px"><span class="rule"></span>♥<h2>The Wedding Events</h2>♥<span class="rule"></span></div>

<section class="abs event" style="left:154px">
  <h3>Main Ceremony</h3>
  <div class="event-row">
    <div class="date-dot"><svg width="14" height="13" viewBox="0 0 14 13"><rect x="1" y="2" width="12" height="10" fill="none" stroke="#fff" stroke-width="1.5"/><line x1="1" y1="5" x2="13" y2="5" stroke="#fff"/></svg>DEC<br>26</div>
    <div class="event-meta">
      <div><svg width="13" height="13" viewBox="0 0 14 14"><circle cx="7" cy="7" r="6" fill="none" stroke="#555" stroke-width="1.4"/><path d="M7 3.5V7h3" fill="none" stroke="#555" stroke-width="1.4"/></svg>3pm - 6pm</div>
      <div><svg width="11" height="15" viewBox="0 0 12 16"><path d="M6 15C2 10 1 8 1 6a5 5 0 0110 0c0 2-1 4-5 9z" fill="#555"/><circle cx="6" cy="6" r="2" fill="#fff"/></svg>48 Ferngrove Lane,<br>Brookvale</div>
    </div>
  </div>
  <p>Duis aute irure dolor in reprehenderit in voluptate velit esse cillum dolore eu fugiat nulla pariatur.</p>
  <span class="read-more">Read More <b>→</b></span>
</section>

<section class="abs event" style="left:459px">
  <h3>Wedding Party</h3>
  <div class="event-row">
    <div class="date-dot"><svg width="14" height="13" viewBox="0 0 14 13"><rect x="1" y="2" width="12" height="10" fill="none" stroke="#fff" stroke-width="1.5"/><line x1="1" y1="5" x2="13" y2="5" stroke="#fff"/></svg>DEC<br>27</div>
    <div class="event-meta">
      <div><svg width="13" height="13" viewBox="0 0 14 14"><circle cx="7" cy="7" r="6" fill="none" stroke="#555" stroke-width="1.4"/><path d="M7 3.5V7h3" fill="none" stroke="#555" stroke-width="1.4"/></svg>3pm - 6pm</div>
      <div><svg width="11" height="15" viewBox="0 0 12 16"><path d="M6 15C2 10 1 8 1 6a5 5 0 0110 0c0 2-1 4-5 9z" fill="#555"/><circle cx="6" cy="6" r="2" fill="#fff"/></svg>48 Ferngrove Lane,<br>Brookvale</div>
    </div>
  </div>
  <p>Duis aute irure dolor in reprehenderit in voluptate velit esse cillum dolore eu fugiat nulla pariatur.</p>
  <span class="read-more">Read More <b>→</b></span>
</section>

<section class="abs event" style="left:765px">
  <h3>Wedding Dinner</h3>
  <div class="event-row">
    <div class="date-dot"><svg width="14" height="13" viewBox="0 0 14 13"><rect x="1" y="2" width="12" height="10" fill="none" stroke="#fff" stroke-width="1.5"/><line x1="1" y1="5" x2="13" y2="5" stroke="#fff"/></svg>DEC<br>28</div>
    <div class="event-meta">
      <div><svg width="13" height="13" viewBox="0 0 14 14"><circle cx="7" cy="7" r="6" fill="none" stroke="#555" stroke-width="1.4"/><path d="M7 3.5V7h3" fill="none" stroke="#555" stroke-width="1.4"/></svg>3pm - 6pm</div>
      <div><svg width="11" height="15" viewBox="0 0 12 16"><path d="M6 15C2 10 1 8 1 6a5 5 0 0110 0c0 2-1 4-5 9z" fill="#555"/><circle cx="6" cy="6" r="2" fill="#fff"/></svg>48 Ferngrove Lane,<br>Brookvale</div>
    </div>
  </div>
  <p>Duis aute irure dolor in reprehenderit in voluptate velit esse cillum dolore eu fugiat nulla pariatur.</p>
  <span class="read-more">Read More <b>→</b></span>
</section>

<div class="abs sec-title" style="top:2420px"><span class="rule"></span>♥<h2>Photo Album</h2>♥<span class="rule"></span></div>
<div class="abs album" role="img" aria-label="Photo of the bride and groom touching foreheads in a garden"></div>
<svg class="abs arrow" style="left:98px" width="30" height="60" viewBox="0 0 30 60"><path d="M26 2L4 30l22 28" fill="none" stroke="#fff" stroke-width="3"/></svg>
<svg class="abs arrow" style="left:1072px" width="30" height="60" viewBox="0 0 30 60"><path d="M4 2l22 28L4 58" fill="none" stroke="#a5ce39" stroke-width="3"/></svg>

<svg class="abs thumb" style="left:170px" width="176" height="140" viewBox="0 0 100 88" role="img" aria-label="Black and white wedding photo thumbnail"><path d="M50 84C21 61 4 46 4 27 4 14 14 4 27 4c10 0 18 6 23 14C55 10 63 4 73 4c13 0 23 10 23 23 0 19-17 34-46 57z" fill="#7b7b7b" stroke="#fff" stroke-width="3" stroke-dasharray="5 3"/></svg>
<svg class="abs thumb" style="left:401px" width="176" height="140" viewBox="0 0 100 88" role="img" aria-label="Black and white wedding photo thumbnail"><path d="M50 84C21 61 4 46 4 27 4 14 14 4 27 4c10 0 18 6 23 14C55 10 63 4 73 4c13 0 23 10 23 23 0 19-17 34-46 57z" fill="#8e8e8e" stroke="#fff" stroke-width="3" stroke-dasharray="5 3"/></svg>
<svg class="abs thumb" style="left:624px" width="176" height="140" viewBox="0 0 100 88" role="img" aria-label="Black and white wedding photo thumbnail"><path d="M50 84C21 61 4 46 4 27 4 14 14 4 27 4c10 0 18 6 23 14C55 10 63 4 73 4c13 0 23 10 23 23 0 19-17 34-46 57z" fill="#6e6e6e" stroke="#fff" stroke-width="3" stroke-dasharray="5 3"/></svg>
<svg class="abs thumb" style="left:855px" width="176" height="140" viewBox="0 0 100 88" role="img" aria-label="Black and white wedding photo thumbnail"><path d="M50 84C21 61 4 46 4 27 4 14 14 4 27 4c10 0 18 6 23 14C55 10 63 4 73 4c13 0 23 10 23 23 0 19-17 34-46 57z" fill="#959595" stroke="#fff" stroke-width="3" stroke-dasharray="5 3"/></svg>

<div class="abs sec-title" style="top:3232px"><span class="rule"></span>♥<h2>Are you attending?</h2>♥<span class="rule"></span></div>
<div class="abs field" style="left:154px;width:284px">Enter Your name ...</div>
<div class="abs field" style="left:457px;width:281px">Enter Your email ...</div>
<div class="abs field" style="left:765px;width:278px;display:flex;justify-content:space-between">I am attending all events<svg width="12" height="8" viewBox="0 0 12 8"><path d="M1 1l5 5 5-5" fill="none" stroke="#666" stroke-width="2"/></svg></div>
<div class="abs send">SEND</div>

<div class="abs footer" role="img" aria-label="Group photo of the wedding party on a porch"></div>
<p class="abs farewell script">See you on 26th May 2018</p>
<p class="abs with script">With ♥ L&amp;D</p>
<p class="abs copy">© Wedding 2018 • kolvarenplitz.ch • All Rights Reserved</p>

</body>
</html>
```